Corporate Design für einen Rebell in der Gesundheitsbranche
Zielgruppe
Wir denken Gesundheit neu. Wir räumen mit Althergebrachtem auf und helfen den Menschen, sich wieder aktiv um ihre Gesundheit zu kümmern.
Unser Unternehmen entwickelt, produziert und vertreibt Produkte mit denen Menschen ihre Gesundheit erhalten, verbessern oder wiederherstellen können.
Die Produkte sind für Endverbraucher bestimmt, der Vertrieb erfolgt als B2B an Schuhfabrikanten, große Schuhhäuser und Orthopädiefachgeschäfte sowohl in Deutschland als auch international.
Dabei sind die zentralen Elemente
1. Fußgesundheit und Körperhaltung: aktivierende Schuh-Einlagen, Haltungs-, Gang- und Laufanalysen
2. Einsatz von moderner Technologie (3D Scans, Sensorik, Videoanalse, Ergometer)
3. Produktentwicklung basiert auf aktuellen Forschungsergebnissen im Bereich Neuro-Physiologie und Sensomotorik.
Das erste zentrale Produkt, welches kurz vor der Markteinführung steht ist die Vela Trimo Base(R), eine patentierte sensomotorische Einlage, die über eine neuro-physiologische Wirkungsweise die Fußgesundheit verbessern kann und Haltungsbeschwerden sowie -schmerzen reduziert.
Das gesamte Produktkonzept basiert auf einem neuen, zukunftsweisenden Verständnis der Zusammenhänge zwischen Muskeln, Bindegewebe, Füßen, Neurophysiologie, Wissenschaft und Medizin.
Das Design sollte vor allem Erwachsenen gefallen und Gesundheit, Innovation Ganzheitlichkeit vermitteln.
Aufgabenstellung
Das Logo sollte folgende Komponenten enthalten: Gehirn, Fuß oder Füße, Dreieck.
Gehirn: Neurophysiologie
Fuß: Fundament der Haltung
Dreieck: Basiselement in der Architektur (Tensegrity-Modell)
Das Design sollte stilisierend sein. Die drei Elemente sollten mit möglichst wenigen stilisierenden Federstrichen erkennbar sein.
Das Logo sollte vom Firmennamen abtrennbar sein, um es separat zur Wiedererkennung zu nutzen, auch ohne Firmenname.
Seriosität und Schnörkellosigkeit ist ein wichtiger Aspekt. Wir sehen unsere Firma aber auch als Rebell, da wir die vorherrschende Meinung in der Orthopädie grundlegend umkrempeln werden.
Wir möchten also auch Innovation, Wissenschaftlichkeit und eine neue Art über Gesundheit zu denken mit dem Design vermitteln.

```html
<!DOCTYPE html>
<html lang="de">
<head>
<meta charset="utf-8">
<title>Kineva – Geschäftsausstattung</title>
<link href="https://fonts.googleapis.com/css2?family=Montserrat:wght@400;500;600&display=swap" rel="stylesheet">
<style>
:root{
  --teal:#20bfca;
  --ink:#3c3c3c;
  --grey:#8a8a8a;
  --soft:#c9c9c9;
  --faint:#efefef;
  --paper:#ffffff;
  --board:#efefed;
  --font:"Montserrat", Arial, sans-serif;
}
*{box-sizing:border-box;margin:0;padding:0}
html,body{width:1200px;height:1200px;overflow:hidden}
body{background:var(--paper);font-family:var(--font);color:var(--ink);position:relative}
.board{position:absolute;left:0;top:31px;width:1200px;height:1138px;background:linear-gradient(180deg,#f6f6f5,var(--board))}
.item{position:absolute;background:var(--paper);box-shadow:0 1px 3px rgba(0,0,0,.18);overflow:hidden}
.label{position:absolute;font-size:12px;color:#222}
.mark{display:flex;flex-direction:column;align-items:center;position:absolute}
.mark .dot{border-radius:50%;background:var(--teal)}
.mark .name{color:var(--teal);font-weight:600;letter-spacing:.04em;line-height:1}
.mark .tag{color:var(--ink);line-height:1;letter-spacing:.08em}
.dot-grey{border-radius:50%;background:var(--soft);position:absolute}
.dot-faint{border-radius:50%;background:var(--faint);position:absolute}
.bar{position:absolute;background:var(--teal)}
.web{position:absolute;font-size:5.5px;letter-spacing:.35em;color:var(--grey)}
.contact{position:absolute;font-size:3.6px;line-height:1.55;color:var(--grey)}
.contact.right{text-align:right}
.icon{position:absolute;width:3px;height:3px;border-radius:50%;background:var(--teal)}
.person{position:absolute;font-size:11px;font-weight:500;color:var(--ink)}
.role{font-size:5px;color:var(--teal);letter-spacing:.06em;font-weight:500}
.info{position:absolute;font-size:4.6px;line-height:1.5;color:var(--grey)}
.info b{font-weight:600;color:var(--grey)}
.info .t{color:var(--teal)}
.addr{position:absolute;font-size:5px;color:var(--grey);letter-spacing:.04em;border-bottom:.6px solid var(--grey);padding-bottom:3px}
.fold{position:absolute;left:0;width:8px;height:.6px;background:var(--soft)}
.foot{position:absolute;font-size:3.6px;line-height:1.4;color:var(--grey)}
</style>
</head>
<body>
<div class="board"></div>

<!-- main logo card -->
<section class="item" style="left:70px;top:147px;width:331px;height:187px;box-shadow:none">
  <div class="mark" style="left:0;right:0;top:42px">
    <div class="dot" style="width:72px;height:72px"></div>
    <div class="name" style="font-size:22px;margin-top:18px">KINEVA</div>
    <div class="tag" style="font-size:8px;margin-top:3px">Rethinking health</div>
  </div>
</section>

<!-- business cards: front -->
<span class="label" style="left:72px;top:368px">1</span>
<section class="item" style="left:91px;top:366px;width:129px;height:84px">
  <div class="mark" style="left:0;right:0;top:12px">
    <div class="dot" style="width:36px;height:36px"></div>
    <div class="name" style="font-size:11px;margin-top:8px">KINEVA</div>
    <div class="tag" style="font-size:4.5px;margin-top:2px">Rethinking health</div>
  </div>
</section>

<span class="label" style="left:72px;top:469px">2</span>
<section class="item" style="left:91px;top:468px;width:129px;height:84px">
  <div class="dot-grey" style="left:39px;top:8px;width:52px;height:52px;background:var(--teal)"></div>
  <div class="web" style="left:0;right:0;text-align:center;top:72px">www.kineva.de</div>
</section>

<span class="label" style="left:72px;top:570px">3</span>
<section class="item" style="left:91px;top:569px;width:129px;height:84px">
  <div class="mark" style="left:0;right:0;top:6px">
    <div class="dot" style="width:34px;height:34px"></div>
    <div class="name" style="font-size:11px;margin-top:7px">KINEVA</div>
    <div class="tag" style="font-size:4.5px;margin-top:2px">Rethinking health</div>
  </div>
  <div class="web" style="left:0;right:0;text-align:center;top:73px">www.kineva.de</div>
</section>

<span class="label" style="left:72px;top:675px">4</span>
<section class="item" style="left:91px;top:673px;width:129px;height:84px;background:var(--teal)">
  <div class="dot-grey" style="left:38px;top:13px;width:52px;height:52px;background:#fff"></div>
  <div class="web" style="left:0;right:0;text-align:center;top:73px;color:#fff">www.kineva.de</div>
</section>

<!-- business cards: back -->
<span class="label" style="left:240px;top:368px">a</span>
<section class="item" style="left:259px;top:366px;width:132px;height:84px">
  <div class="person" style="left:9px;top:12px">Jan Muster<div class="role" style="font-size:4px">INHABER</div></div>
  <div class="dot-grey" style="left:12px;top:38px;width:36px;height:36px"></div>
  <div class="contact right" style="right:20px;top:30px">Kineva<br>XXXXXXstr. 1<br>00000 Germany<br><br>T. +49 0000 - 000 00 00<br>F. +49 000 - 000 00 00<br><br>info@kineva.de<br><br>www.kineva.de</div>
  <span class="icon" style="right:11px;top:31px"></span>
  <span class="icon" style="right:11px;top:52px"></span>
  <span class="icon" style="right:11px;top:66px"></span>
  <span class="icon" style="right:11px;top:76px"></span>
  <div class="bar" style="right:0;top:27px;width:7px;height:57px"></div>
</section>

<span class="label" style="left:240px;top:468px">b</span>
<section class="item" style="left:257px;top:466px;width:132px;height:84px">
  <div class="bar" style="left:0;top:0;width:7px;height:32px"></div>
  <div class="person" style="left:14px;top:12px">Jan Muster <span class="role" style="font-size:7px;color:var(--teal);font-weight:400">| INHABER</span></div>
  <div class="info" style="left:10px;top:47px"><b>Kineva</b><br>XXXXXXstr. 1<br>00000 Germany</div>
  <div class="info" style="left:64px;top:47px"><span class="t">•</span> +49 0000 - 000 00 00<br><span class="t">•</span> +49 0000 - 000 00 00<br><span class="t">•</span> info@kineva.de<br><span class="t">•</span> www.kineva.de</div>
</section>

<span class="label" style="left:240px;top:573px">c</span>
<section class="item" style="left:257px;top:571px;width:132px;height:84px">
  <div class="dot-grey" style="left:10px;top:6px;width:36px;height:36px"></div>
  <div class="person" style="left:62px;top:21px;font-size:12px">Jan Muster<div class="role">INHABER</div></div>
  <div class="info" style="left:6px;top:49px"><b>Kineva</b><br>XXXXXXstr. 1<br>00000 Germany</div>
  <div class="info" style="left:62px;top:49px"><span class="t">•</span> +49 0000 - 000 00 00<br><span class="t">•</span> +49 0000 - 000 00 00<br><span class="t">•</span> info@kineva.de<br><span class="t">•</span> www.kineva.de</div>
</section>

<span class="label" style="left:240px;top:677px">d</span>
<section class="item" style="left:257px;top:674px;width:132px;height:84px">
  <div class="mark" style="left:5px;width:52px;top:5px">
    <div class="dot" style="width:20px;height:20px"></div>
    <div class="name" style="font-size:7px;margin-top:5px">KINEVA</div>
  </div>
  <div class="person" style="left:63px;top:26px;font-size:10px">Jan Muster<div class="role" style="font-size:4.5px">INHABER</div></div>
  <div class="info" style="left:6px;top:49px"><b>Kineva</b><br>XXXXXXstr. 1<br>00000 Germany</div>
  <div class="info" style="left:62px;top:49px"><span class="t">•</span> +49 0000 - 000 00 00<br><span class="t">•</span> +49 0000 - 000 00 00<br><span class="t">•</span> info@kineva.de<br><span class="t">•</span> www.kineva.de</div>
</section>

<!-- letterhead 1 -->
<span class="label" style="left:435px;top:97px">1</span>
<section class="item" style="left:451px;top:93px;width:320px;height:452px">
  <div class="mark" style="left:19px;width:78px;top:9px">
    <div class="dot" style="width:36px;height:36px"></div>
    <div class="name" style="font-size:11px;margin-top:6px">KINEVA</div>
    <div class="tag" style="font-size:4px;margin-top:2px">Rethinking health</div>
  </div>
  <div class="contact right" style="right:23px;top:21px">Kineva<br>XXXXXXstr. 1<br>00000 Germany<br><br>T. +49 0000 - 000 00 00<br>F. +49 0000 - 000 00 00<br><br>info@kineva.de<br><br>www.kineva.de</div>
  <span class="icon" style="right:13px;top:22px"></span>
  <span class="icon" style="right:13px;top:43px"></span>
  <span class="icon" style="right:13px;top:56px"></span>
  <span class="icon" style="right:13px;top:67px"></span>
  <div class="bar" style="right:0;top:15px;width:8px;height:60px"></div>
  <div class="addr" style="left:18px;top:80px">Kineva | XXXstraße 1 - 000000 Germany</div>
  <div class="fold" style="top:160px"></div>
  <div class="fold" style="top:226px"></div>
  <div class="fold" style="top:318px"></div>
  <div class="foot" style="left:26px;top:424px">Sitz der Gesellschaft<br>Geschäftsführer<br>Amtsgericht<br>USt-ID-Nr</div>
  <div class="foot" style="left:80px;top:424px">XXXXXXXXXX<br>Jan Muster<br>HRB XXXXXXXXXX<br>DE 000 000 000</div>
  <div class="foot" style="left:155px;top:424px">Bank<br>IBAN<br>BIC</div>
  <div class="foot" style="left:175px;top:424px">xxxxxxxxxxxxxxxxxxxxxx<br>DE00 0000 0000 0000 0000 00<br>xxxxxxxxxx</div>
  <div class="dot-grey" style="left:258px;top:412px;width:36px;height:36px"></div>
  <div class="bar" style="right:0;top:407px;width:8px;height:45px"></div>
</section>

<!-- letterhead 2 -->
<span class="label" style="left:801px;top:97px">2</span>
<section class="item" style="left:817px;top:93px;width:320px;height:452px">
  <div class="mark" style="left:0;right:0;top:7px">
    <div class="dot" style="width:36px;height:36px"></div>
    <div class="name" style="font-size:11px;margin-top:6px">KINEVA</div>
    <div class="tag" style="font-size:4px;margin-top:2px">Rethinking health</div>
  </div>
  <div class="dot-faint" style="left:71px;top:178px;width:200px;height:200px"></div>
  <div class="contact right" style="right:23px;top:52px">Kineva<br>XXXXXXstr. 1<br>00000 Germany<br><br>T. +49 0000 - 000 00 00<br>F. +49 0000 - 000 00 00<br><br>info@kineva.de<br><br>www.kineva.de</div>
  <span class="icon" style="right:13px;top:52px"></span>
  <span class="icon" style="right:13px;top:73px"></span>
  <span class="icon" style="right:13px;top:86px"></span>
  <span class="icon" style="right:13px;top:97px"></span>
  <div class="bar" style="right:0;top:44px;width:7px;height:61px"></div>
  <div class="addr" style="left:17px;top:80px">Kineva | XXXstraße 1 - 000000 Germany</div>
  <div class="fold" style="top:160px"></div>
  <div class="fold" style="top:226px"></div>
  <div class="fold" style="top:318px"></div>
  <div class="foot" style="left:56px;top:424px">Sitz der Gesellschaft<br>Geschäftsführer<br>Amtsgericht<br>USt-ID-Nr</div>
  <div class="foot" style="left:109px;top:424px">XXXXXXXXXX<br>Jan Muster<br>HRB XXXXXXXXXX<br>DE 000 000 000</div>
  <div class="foot" style="left:183px;top:424px">Bank<br>IBAN<br>BIC</div>
  <div class="foot" style="left:204px;top:424px">xxxxxxxxxxxxxxxxxxxxxx<br>DE00 0000 0000 0000 0000 00<br>xxxxxxxxxx</div>
  <div class="bar" style="left:0;top:418px;width:7px;height:34px"></div>
</section>

<!-- envelope 1 -->
<span class="label" style="left:435px;top:590px">1</span>
<section class="item" style="left:455px;top:576px;width:334px;height:167px">
  <div class="mark" style="left:4px;width:67px;top:6px">
    <div class="dot" style="width:30px;height:30px"></div>
    <div class="name" style="font-size:9.5px;margin-top:6px">KINEVA</div>
    <div class="tag" style="font-size:3.6px;margin-top:2px">Rethinking health</div>
  </div>
  <div class="dot-faint" style="left:193px;top:22px;width:124px;height:124px"></div>
  <div class="web" style="right:14px;top:157px;font-size:6px;letter-spacing:.2em">www.kineva.de</div>
  <div class="bar" style="right:0;top:143px;width:7px;height:24px"></div>
</section>

<!-- envelope 2 -->
<span class="label" style="left:439px;top:789px">2</span>
<section class="item" style="left:459px;top:770px;width:334px;height:168px">
  <div class="mark" style="left:5px;width:67px;top:7px">
    <div class="dot" style="width:30px;height:30px"></div>
    <div class="name" style="font-size:9.5px;margin-top:6px">KINEVA</div>
    <div class="tag" style="font-size:3.6px;margin-top:2px">Rethinking health</div>
  </div>
  <div style="position:absolute;left:31px;top:74px;width:152px;height:67px;border-radius:5px;background:#d1d1d1"></div>
  <div class="dot-grey" style="left:233px;top:62px;width:46px;height:46px"></div>
  <div class="web" style="left:205px;top:136px;font-size:8px;letter-spacing:.2em">www.kineva.de</div>
  <div class="bar" style="right:0;top:0;width:7px;height:168px"></div>
</section>

<!-- envelope 3 -->
<span class="label" style="left:439px;top:985px">3</span>
<section class="item" style="left:459px;top:975px;width:334px;height:170px">
  <svg style="position:absolute;left:0;top:0" width="334" height="60" viewBox="0 0 334 60" aria-hidden="true">
    <path d="M0 0 H334 L326 48 Q324 59 312 59 H22 Q10 59 8 48 Z" fill="var(--teal)"/>
  </svg>
  <div class="dot-grey" style="left:152px;top:8px;width:30px;height:30px;background:#fff"></div>
  <div class="web" style="left:0;right:0;text-align:center;top:47px;color:#fff">www.kineva.de</div>
</section>
</body>
</html>
```